Lumen Path - Fiber Internet to the home postcard

Design a postcard for my company, Lumen Path, using the logo below. On the front of the card:
- No Buffering • No BS
- Second line should be the logo
- $60 / month • 10-Gigs
- lumenpath.net

Color palate should follow the colors in the logo.

Address should say
- Special pricing during construction
- Our best price
- Our fastest speed
- $60 / month • 10-Gigs
- lumenpath.net

Target Market(s)

25 - 55 year olds. Middle income/class. People with kids and pick up trucks

Industry/Entity Type

Fiber Internet Service Provider

Font styles to use
Sans Serif

Colors

Designer to choose colors to be used in the design.

Requirements
Nice to have
• I am open to more creative changes

```html
<!DOCTYPE html>
<html lang="en">
<head>
<meta charset="utf-8">
<title>Lumen Path – Fiber Postcard</title>
<link rel="stylesheet" href="https://fonts.googleapis.com/css2?family=Jost:wght@600;700;800&display=swap">
<style>
  :root {
    --navy: #0f2350;
    --blue-deep: #0b2a4f;
    --blue-mid: #1d5888;
    --blue-light: #2f77a8;
    --green: #7ac143;
    --white: #ffffff;
    --page: #ffffff;
  }
  * { margin: 0; padding: 0; box-sizing: border-box; }
  html, body {
    width: 1200px; height: 1000px; overflow: hidden;
    background: var(--page);
    font-family: "Jost", "Futura", sans-serif;
  }
  .postcard {
    position: absolute; left: 315px; width: 571px; height: 440px;
    box-shadow: 0 1px 4px rgba(0,0,0,0.25);
    overflow: hidden;
  }
  .postcard--front { top: 40px; }
  .postcard--back { top: 519px; height: 441px; background: var(--white); }

  .hero-photo {
    position: absolute; left: 0; top: 0; width: 571px; height: 381px;
    background:
      radial-gradient(ellipse at 75% 55%, rgba(60,110,150,0.55), transparent 60%),
      linear-gradient(160deg, var(--blue-light) 0%, var(--blue-mid) 40%, var(--blue-deep) 100%);
  }
  .hero-content {
    position: absolute; left: 0; top: 0; width: 571px; height: 381px;
    color: var(--white); text-align: center;
  }
  .headline {
    position: absolute; left: 0; width: 100%;
    font-weight: 700; font-size: 62px; line-height: 1; letter-spacing: 0.5px;
  }
  .headline--one { top: 20px; }
  .headline--two { top: 80px; }
  .brand {
    position: absolute; left: 0; top: 160px; width: 100%;
    text-align: center;
  }
  .brand-name { font-weight: 700; font-size: 70px; line-height: 1; letter-spacing: -1px; }
  .offer {
    position: absolute; left: 0; top: 276px; width: 100%;
    display: flex; justify-content: center; align-items: flex-end;
    font-weight: 700; line-height: 1;
  }
  .offer-currency { font-size: 30px; align-self: flex-start; margin-top: 6px; }
  .offer-figure { font-size: 86px; letter-spacing: -1px; }
  .offer-unit { font-size: 34px; margin-bottom: 6px; margin-left: 2px; }
  .offer-divider { width: 3px; height: 76px; background: var(--green); margin: 0 26px 2px; }
  .url-band {
    position: absolute; left: 0; top: 381px; width: 571px; height: 59px;
    background: var(--green); color: var(--white);
    display: flex; align-items: center; justify-content: center;
    font-weight: 700; font-size: 36px;
  }

  .return-block { position: absolute; left: 21px; top: 20px; color: var(--navy); }
  .return-brand { margin-bottom: 12px; }
  .return-brand-name { font-weight: 700; font-size: 30px; line-height: 1; }
  .return-lines { list-style: none; font-weight: 700; font-size: 12.5px; line-height: 16px; }
</style>
</head>
<body>
  <section class="postcard postcard--front">
    <div class="hero-photo" role="img" aria-label="Photo of hands typing on a laptop keyboard, tinted deep blue"></div>
    <div class="hero-content">
      <h1 class="headline headline--one">NO BUFFERING</h1>
      <p class="headline headline--two">NO BS</p>
      <div class="brand">
        <span class="brand-name">Lumen Path</span>
      </div>
      <div class="offer">
        <span class="offer-currency">$</span>
        <span class="offer-figure">60</span>
        <span class="offer-unit">/mo</span>
        <span class="offer-divider"></span>
        <span class="offer-figure">10</span>
        <span class="offer-unit">gigs</span>
      </div>
    </div>
    <div class="url-band">www.lumenpath.net</div>
  </section>

  <section class="postcard postcard--back">
    <div class="return-block">
      <div class="return-brand">
        <span class="return-brand-name">Lumen Path</span>
      </div>
      <ul class="return-lines">
        <li>Special Pricing During Construction</li>
        <li>Our Best Price</li>
        <li>Our Fastest Speed</li>
        <li>$60/month • 10-Gigs</li>
        <li>www.lumenpath.net</li>
      </ul>
    </div>
  </section>
</body>
</html>
```